Verindo Living- Hang tags for Modern Handmade Home Decor products

We need to design some hang tags to use for our products, we want double tags, meaning two tags that go together on one string, two different and coordinating sizes and shapes. We have a logo, what we need is the artwork for these two tags to take to print. One tag will have the logo on one side and company information on the other, the second tag will be for product information. For example, we specialize in handmade pieces from Latin America, on the product tag I want space to write the product info but also a line for what country it's from and what community created it. I'm attaching an image of the shapes of tags that I like, along with a copy of our logo. On the larger company tag I'd like our logo in the center and a color block stripe of the yellow color of our logo at the bottom, on the flip side there will just be text, sort of our company motto. On the narrower longer product info tag I'd like a small logo at the bottom end and space for product information to be written in by hand and on the flip side of this one lines for what country it's from, what community created it and care instructions, again, all information that we will write in by hand. Please let me know if you have questions.

Target Market(s)

Design savvy, house proud, well educated people who travel and appreciate art.

Font styles to use
Sans Serif

Requirements
Must have
• I want it to look graphic, sophisticated and modern. I want to be very legible and clean.
Nice to have
• Clarity, easy to read, and maybe a bit of whimsy or lightheartedness.
Should not have
• Nothing that feels "ethnic" or "crafty:, even though our products are handmade in Latin America they are contemporary and sophisticated, not stereotypical.

```html
<!DOCTYPE html>
<html lang="en">
<head>
<meta charset="utf-8">
<title>Verindo Living – Hang Tags</title>
<link href="https://fonts.googleapis.com/css2?family=Quicksand:wght@400&family=Oswald:wght@300;400;500&family=Montserrat:wght@500&display=swap" rel="stylesheet">
<style>
  :root{
    --bg:#e8e8ea;
    --kraft-light:#ece4cc;
    --rust:#a8631a;
    --rust-dark:#7e4510;
    --gold:#d9a92e;
    --ink:#1a1a1a;
    --ink-soft:#2b2b2b;
    --grey-text:#5b5b5b;
    --cream:#f7efdc;
    --silver:#d8d8d8;
    --rule-dark:rgba(26,26,26,.55);
    --rule-light:rgba(220,220,220,.6);
  }
  *{margin:0;padding:0;box-sizing:border-box}
  html,body{width:1200px;height:813px;overflow:hidden;background:var(--bg)}
  .canvas{position:relative;width:1200px;height:813px;background:var(--bg)}
  .tag{position:absolute}
  .tag-shape{position:absolute;left:0;top:0}
  .layer{position:absolute;left:0;right:0;text-align:center}

  .brand-dot{position:absolute;left:50%;border-radius:50%;background:var(--gold);transform:translateX(-50%)}
  .brand-name{font-family:"Quicksand",sans-serif;font-weight:400;letter-spacing:1px;line-height:1}
  .brand-url{font-family:"Montserrat",sans-serif;font-weight:500;letter-spacing:2.4px;line-height:1}

  /* company tags */
  .tag-company{top:236px;width:247px;height:456px}
  .tag-front{left:58px}
  .tag-back{left:374px}
  .tag-company .brand-name{color:var(--grey-text)}
  .tag-company .brand-url{color:var(--cream);font-size:10px}
  .motto{position:absolute;left:42px;width:178px;top:198px;font-family:"Oswald",sans-serif;font-weight:300;font-size:11.4px;line-height:17.5px;color:#2a2414;text-align:justify}

  /* product tags */
  .tag-product{top:86px;width:204px;height:610px}
  .tag-label{left:666px}
  .tag-care{left:950px}
  .tag-product .brand-name{color:var(--gold)}
  .tag-product .brand-url{color:#e9e9e9;font-size:7px;letter-spacing:1.6px}
  .kicker{font-family:"Oswald",sans-serif;font-weight:500;letter-spacing:.5px;line-height:1}
  .title{font-family:"Oswald",sans-serif;font-weight:400;line-height:1;letter-spacing:.5px}
  .small-cond{font-family:"Oswald",sans-serif;font-weight:300;line-height:1}

  .write-in{position:absolute;display:flex;flex-direction:column;gap:12px}
  .write-row{display:flex;align-items:flex-end;gap:6px;font-family:"Oswald",sans-serif;font-weight:400;font-size:10px;line-height:1;letter-spacing:.4px}
  .write-row .rule{flex:1;height:0;border-bottom:1px solid}
  .tag-label .write-in{left:44px;right:44px;top:436px}
  .tag-label .write-row{color:var(--ink)}
  .tag-label .write-row .rule{border-color:var(--rule-dark)}
  .tag-care .write-in{left:42px;right:42px;top:426px;gap:14px}
  .tag-care .write-row{color:#e2e2e2;font-size:10.5px}
  .tag-care .write-row .rule{border-color:var(--rule-light)}
</style>
</head>
<body>
<main class="canvas">

  <!-- Company tag: front -->
  <section class="tag tag-company tag-front">
    <svg class="tag-shape" width="247" height="456" viewBox="0 0 247 456">
      <defs>
        <linearGradient id="kraftFront" x1="0" y1="0" x2="0" y2="1">
          <stop offset="0" stop-color="#e3d8b8"/>
          <stop offset="1" stop-color="#cdb989"/>
        </linearGradient>
        <radialGradient id="amberWash" cx="0.3" cy="0.5" r="0.6">
          <stop offset="0" stop-color="#f5a81b" stop-opacity="0.9"/>
          <stop offset="1" stop-color="#f5a81b" stop-opacity="0"/>
        </radialGradient>
        <clipPath id="frontClip"><path d="M0,80 Q0,66 14,66 L30,66 L30,46 Q30,34 42,34 L88,34 Q92,0 123,0 Q154,0 158,34 L205,34 Q217,34 217,46 L217,66 L233,66 Q247,66 247,80 L247,446 Q247,456 237,456 L10,456 Q0,456 0,446 Z"/></clipPath>
      </defs>
      <g clip-path="url(#frontClip)">
        <rect width="247" height="456" fill="url(#kraftFront)"/>
        <rect x="24" y="112" width="200" height="250" rx="8" fill="var(--kraft-light)" opacity="0.75"/>
        <rect x="0" y="300" width="190" height="120" fill="url(#amberWash)" role="img" aria-label="Orange brush-stroke texture"/>
        <rect x="0" y="416" width="247" height="40" fill="var(--rust)"/>
      </g>
      <path d="M0,80 Q0,66 14,66 L30,66 L30,46 Q30,34 42,34 L88,34 Q92,0 123,0 Q154,0 158,34 L205,34 Q217,34 217,46 L217,66 L233,66 Q247,66 247,80 L247,446 Q247,456 237,456 L10,456 Q0,456 0,446 Z" fill="none" stroke="var(--rust-dark)" stroke-width="1.5"/>
      <circle cx="123" cy="38" r="18" fill="#8d8d8d"/>
      <circle cx="123" cy="38" r="12" fill="var(--bg)"/>
    </svg>
    <span class="brand-dot" style="top:208px;width:30px;height:30px"></span>
    <div class="layer brand-name" style="top:256px;font-size:36px">verindo</div>
    <div class="layer brand-url" style="top:430px">www.verindoliving.com</div>
  </section>

  <!-- Company tag: back -->
  <section class="tag tag-company tag-back">
    <svg class="tag-shape" width="247" height="456" viewBox="0 0 247 456">
      <defs>
        <linearGradient id="kraftBack" x1="0" y1="0" x2="0" y2="1">
          <stop offset="0" stop-color="#d8c48f"/>
          <stop offset="1" stop-color="#c4a860"/>
        </linearGradient>
        <radialGradient id="amberWashBack" cx="0.3" cy="0.55" r="0.6">
          <stop offset="0" stop-color="#f5a81b" stop-opacity="0.85"/>
          <stop offset="1" stop-color="#f5a81b" stop-opacity="0"/>
        </radialGradient>
        <clipPath id="backClip"><path d="M0,80 Q0,66 14,66 L30,66 L30,46 Q30,34 42,34 L88,34 Q92,0 123,0 Q154,0 158,34 L205,34 Q217,34 217,46 L217,66 L233,66 Q247,66 247,80 L247,446 Q247,456 237,456 L10,456 Q0,456 0,446 Z"/></clipPath>
      </defs>
      <g clip-path="url(#backClip)">
        <rect width="247" height="456" fill="url(#kraftBack)"/>
        <rect x="0" y="0" width="247" height="140" fill="#e1d3a9"/>
        <rect x="0" y="140" width="247" height="42" fill="#e6dbb8"/>
        <rect x="0" y="300" width="200" height="120" fill="url(#amberWashBack)" role="img" aria-label="Orange brush-stroke texture"/>
        <rect x="0" y="416" width="247" height="40" fill="var(--rust)"/>
      </g>
      <path d="M0,80 Q0,66 14,66 L30,66 L30,46 Q30,34 42,34 L88,34 Q92,0 123,0 Q154,0 158,34 L205,34 Q217,34 217,46 L217,66 L233,66 Q247,66 247,80 L247,446 Q247,456 237,456 L10,456 Q0,456 0,446 Z" fill="none" stroke="var(--rust-dark)" stroke-width="1.5"/>
      <circle cx="123" cy="38" r="18" fill="#8d8d8d"/>
      <circle cx="123" cy="38" r="12" fill="var(--bg)"/>
    </svg>
    <span class="brand-dot" style="top:98px;width:28px;height:28px"></span>
    <div class="layer brand-name" style="top:148px;font-size:30px">verindo</div>
    <p class="motto">Verindo Living is a home décor studio co-creating beautiful and unique handmade pieces with artisan partners throughout Latin America, made by hand and heart and designed for the modern home.Please sign up for our mailing list and join us on our</p>
    <div class="layer brand-url" style="top:430px">www.verindoliving.com</div>
  </section>

  <!-- Product tag: label side -->
  <section class="tag tag-product tag-label">
    <svg class="tag-shape" width="204" height="610" viewBox="0 0 204 610">
      <defs>
        <linearGradient id="goldPanel" x1="0" y1="0" x2="1" y2="1">
          <stop offset="0" stop-color="#b98419"/>
          <stop offset="0.35" stop-color="#f3d273"/>
          <stop offset="0.65" stop-color="#e0b13c"/>
          <stop offset="1" stop-color="#a87815"/>
        </linearGradient>
        <linearGradient id="goldLine" x1="0" y1="0" x2="1" y2="1">
          <stop offset="0" stop-color="#f1cf6a"/>
          <stop offset="1" stop-color="#a97a16"/>
        </linearGradient>
      </defs>
      <path d="M0,58 Q0,40 18,40 L52,40 Q60,40 62,30 Q70,0 102,0 Q134,0 142,30 Q144,40 152,40 L186,40 Q204,40 204,58 L204,592 Q204,610 186,610 L18,610 Q0,610 0,592 Z" fill="var(--ink)"/>
      <path d="M10,68 Q10,52 26,52 L58,52 Q68,52 70,42 Q76,12 102,12 Q128,12 134,42 Q136,52 146,52 L178,52 Q194,52 194,68 L194,584 Q194,600 178,600 L26,600 Q10,600 10,584 Z" fill="none" stroke="url(#goldLine)" stroke-width="1.5"/>
      <rect x="28" y="238" width="148" height="40" fill="#6f5214" role="img" aria-label="Gold filigree ornament"/>
      <rect x="28" y="530" width="148" height="38" fill="#6f5214" role="img" aria-label="Gold filigree ornament"/>
      <rect x="32" y="262" width="140" height="284" rx="14" fill="url(#goldPanel)"/>
      <g stroke="var(--ink)" stroke-width="1">
        <line x1="48" y1="332" x2="96" y2="332"/><line x1="108" y1="332" x2="156" y2="332"/>
      </g>
      <rect x="99" y="329" width="6" height="6" transform="rotate(45 102 332)" fill="var(--ink)"/>
      <circle cx="102" cy="42" r="16" fill="#9a9a9a"/>
      <circle cx="102" cy="42" r="10" fill="#d5d5d5"/>
    </svg>
    <span class="brand-dot" style="top:114px;width:26px;height:26px"></span>
    <div class="layer brand-name" style="top:172px;font-size:26px">verindo</div>
    <div class="layer brand-url" style="top:204px">www.verindoliving.com</div>
    <span class="brand-dot" style="top:272px;width:18px;height:18px;background:var(--ink)"></span>
    <div class="layer kicker" style="top:302px;font-size:17px;color:var(--ink)">Place Your</div>
    <div class="layer title" style="top:340px;font-size:26px;color:var(--ink)">Product</div>
    <div class="layer title" style="top:368px;font-size:32px;color:var(--ink)">Name</div>
    <div class="layer small-cond" style="top:413px;font-size:11px;color:var(--ink)">Place your text here</div>
    <div class="write-in">
      <div class="write-row"><span>Item</span><span class="rule"></span></div>
      <div class="write-row"><span>Size</span><span class="rule"></span></div>
      <div class="write-row"><span>Material</span><span class="rule"></span></div>
      <div class="write-row"><span class="rule"></span></div>
    </div>
  </section>

  <!-- Product tag: care side -->
  <section class="tag tag-product tag-care">
    <svg class="tag-shape" width="204" height="610" viewBox="0 0 204 610">
      <defs>
        <linearGradient id="goldLine2" x1="0" y1="0" x2="1" y2="1">
          <stop offset="0" stop-color="#f1cf6a"/>
          <stop offset="1" stop-color="#a97a16"/>
        </linearGradient>
      </defs>
      <path d="M0,58 Q0,40 18,40 L52,40 Q60,40 62,30 Q70,0 102,0 Q134,0 142,30 Q144,40 152,40 L186,40 Q204,40 204,58 L204,592 Q204,610 186,610 L18,610 Q0,610 0,592 Z" fill="var(--ink-soft)"/>
      <rect x="24" y="74" width="156" height="60" fill="#5e4612" role="img" aria-label="Gold filigree ornament"/>
      <rect x="24" y="538" width="156" height="56" fill="#5e4612" role="img" aria-label="Gold filigree ornament"/>
      <rect x="28" y="134" width="148" height="404" rx="10" fill="none" stroke="url(#goldLine2)" stroke-width="2"/>
      <g stroke="var(--silver)" stroke-width="1">
        <line x1="42" y1="308" x2="96" y2="308"/><line x1="108" y1="308" x2="162" y2="308"/>
        <line x1="42" y1="386" x2="96" y2="386"/><line x1="108" y1="386" x2="162" y2="386"/>
      </g>
      <rect x="99" y="305" width="6" height="6" transform="rotate(45 102 308)" fill="var(--silver)"/>
      <rect x="99" y="383" width="6" height="6" transform="rotate(45 102 386)" fill="var(--silver)"/>
      <circle cx="102" cy="42" r="16" fill="#9a9a9a"/>
      <circle cx="102" cy="42" r="10" fill="#d5d5d5"/>
    </svg>
    <span class="brand-dot" style="top:150px;width:26px;height:26px"></span>
    <div class="layer brand-name" style="top:204px;font-size:26px">verindo</div>
    <div class="layer brand-url" style="top:237px">www.verindoliving.com</div>
    <div class="layer kicker" style="top:274px;font-size:20px;color:#e4e4e4">Instruction</div>
    <div class="layer title" style="top:316px;font-size:28px;color:#dcdcdc">Product</div>
    <div class="layer title" style="top:345px;font-size:34px;color:#dcdcdc">Name</div>
    <div class="layer small-cond" style="top:398px;font-size:12px;color:#e2e2e2">Place your text here</div>
    <div class="write-in">
      <div class="write-row"><span>Country</span><span class="rule"></span></div>
      <div class="write-row"><span>Community</span><span class="rule"></span></div>
      <div class="write-row"><span>Care</span><span class="rule"></span></div>
      <div class="write-row"><span class="rule"></span></div>
      <div class="write-row"><span class="rule"></span></div>
    </div>
  </section>

</main>
</body>
</html>
```